Graphic Design Larkhollow Book Description

There is a book on Larkhollow that is my competitor that has a large graphic design as part of the description for the book and I want a similar thing for my book to make it stand out more.

My competitors book is here: https://www.larkhollow-books.example/Tidal-Chemistry-Starters-Grasping-Walkthrough/item/K47RZTX902/

My book is here: https://www.larkhollow-books.example/Tidal-Chemistry-Groundwork-Dynamics-Interlinking/item/K3P8WQE27T/

You can see the kind of thing I am looking for on the book listing but I have attached an image below.

Thanks

Owen

```html
<!DOCTYPE html>
<html lang="en">
<head>
<meta charset="utf-8">
<title>Quantum Physics – Book Description Graphic</title>
<link href="https://fonts.googleapis.com/css2?family=Bebas+Neue&family=Poppins:wght@400;500;600;700&display=swap" rel="stylesheet">
<style>
  :root{
    --backdrop:#b9b9b9;
    --ink:#1d1d22;
    --night:#1b1c24;
    --night-deep:#121318;
    --yellow:#f1e52a;
    --yellow-soft:#e9dc25;
    --white:#ffffff;
    --card-grey:#e2e2e2;
    --red:#d8262e;
    --gold:#e7b53a;
    --display:"Bebas Neue", "Oswald", sans-serif;
    --body:"Poppins", "Helvetica Neue", sans-serif;
  }
  *{box-sizing:border-box;margin:0;padding:0}
  html,body{width:798px;height:1200px;overflow:hidden}
  body{background:var(--backdrop);font-family:var(--body);position:relative}
  .sheet{position:absolute;left:55px;top:51px;width:688px;height:1102px;background:var(--white);overflow:hidden}

  /* hero */
  .hero{position:absolute;left:0;top:0;width:688px;height:438px;
    background:radial-gradient(ellipse at 70% 35%, #3a3445 0%, transparent 55%),
               radial-gradient(ellipse at 20% 80%, #3b2a22 0%, transparent 50%),
               linear-gradient(160deg,#23242d 0%,var(--night-deep) 100%)}
  .hero-books{position:absolute;left:42px;top:82px;width:236px;height:353px;
    background:linear-gradient(100deg,#e9e9e9 0 8%,var(--yellow) 8% 100%);box-shadow:6px 8px 18px rgba(0,0,0,.5)}
  .headline{position:absolute;left:310px;top:50px;color:var(--white)}
  .headline .big{font-family:var(--display);font-size:56px;line-height:.9;letter-spacing:.5px}
  .headline .accent{font-size:25px;font-weight:500;color:var(--yellow);line-height:1;margin-top:2px;letter-spacing:.3px}
  .headline .mid{font-size:24px;font-weight:500;line-height:1;letter-spacing:.3px}
  .headline .title{font-family:var(--display);font-size:55px;line-height:.85;margin-top:2px}
  .open-book{position:absolute;left:278px;top:201px;width:334px;height:247px;
    background:linear-gradient(90deg,#f4f4f4 0%,#ffffff 45%,#d8d8d8 50%,#ffffff 55%,#efefef 100%);
    box-shadow:0 6px 16px rgba(0,0,0,.45);transform:skewY(-2deg);z-index:2}
  .seal{position:absolute;left:536px;top:196px;width:106px;height:106px;border-radius:50%;
    background:radial-gradient(circle,#f6d36b 0%,var(--gold) 70%,#b8842a 100%);z-index:3;
    display:flex;align-items:center;justify-content:center}
  .seal-inner{width:80px;height:80px;border-radius:50%;background:radial-gradient(circle,#d92a23,#a9130f);
    border:2px dotted #ffe6a0;color:var(--white);text-align:center;display:flex;flex-direction:column;justify-content:center;line-height:1}
  .seal-inner .script{font-style:italic;font-weight:600;color:#ffcf4a;font-size:14px}
  .seal-inner .big{font-weight:700;font-size:11px}
  .seal-inner .small{font-size:7px;font-weight:500}
  .ribbon{position:absolute;left:462px;top:400px;width:157px;height:40px;background:var(--red);z-index:3;
    transform:rotate(3deg);border-radius:3px 3px 10px 3px;color:var(--white);text-align:center;line-height:1;padding-top:5px;
    box-shadow:0 3px 6px rgba(0,0,0,.35)}
  .ribbon .a{font-size:10px;letter-spacing:1.5px;color:#ffd9a0}
  .ribbon .b{font-size:11px;font-weight:700}
  .ribbon .c{font-size:6.5px;font-weight:500}

  /* topic cards */
  .card{position:absolute;top:456px;width:134px;height:250px;border-radius:8px;overflow:hidden;background:var(--card-grey)}
  .card-head{height:107px;display:flex;flex-direction:column;justify-content:center;align-items:center;
    font-family:var(--display);font-size:25px;line-height:.98;text-align:center}
  .card-head.dark{background:radial-gradient(ellipse at 50% 50%,#2d2b3a,#0e0e13);color:var(--white)}
  .card-head.dark em{font-style:normal;color:var(--yellow)}
  .card-head.light{background:radial-gradient(ellipse at 50% 40%,#f7ef6a,var(--yellow-soft));color:var(--ink)}
  .card-head .thin{font-weight:400;opacity:.95}
  .card-body{padding:14px 6px 0;font-size:12.2px;line-height:1.15;text-align:center;color:var(--ink)}

  /* contents */
  .contents{position:absolute;left:0;top:721px;width:688px;height:381px;
    background:radial-gradient(ellipse at 75% 40%,#3a3a44 0%,transparent 60%),linear-gradient(180deg,#262730,#1c1d23)}
  .contents h2{position:absolute;left:49px;top:14px;font-family:var(--display);font-weight:400;font-size:34px;color:var(--white);letter-spacing:.3px}
  .chapter{position:absolute;left:51px;width:246px;border:1px solid var(--yellow);border-radius:5px;
    display:flex;align-items:center;gap:9px;padding:0 8px;color:var(--white);font-size:10.8px;line-height:1.15}
  .chapter svg{flex:none}
  .bottom-books{position:absolute;left:345px;top:32px;width:290px;height:316px;
    background:linear-gradient(100deg,transparent 0 2%,#ece24a 2% 40%,var(--yellow) 40% 100%);
    clip-path:polygon(0 12%,58% 0,58% 8%,100% 8%,100% 100%,38% 100%,38% 92%,14% 96%);
    box-shadow:0 6px 16px rgba(0,0,0,.5)}
</style>
</head>
<body>
<main class="sheet">
  <section class="hero">
    <div class="hero-books" role="img" aria-label="Paperback mockup of Quantum Physics by Elias Fenwick, yellow cover with atom symbol, back cover behind"></div>
    <div class="headline">
      <div class="big">EMBARK ON A</div>
      <div class="accent">MIND-BENDING JOURNEY</div>
      <div class="mid">INTO THE REALM OF</div>
      <div class="title">QUANTUM PHYSICS</div>
    </div>
    <div class="open-book" role="img" aria-label="Open book showing Chapter 1: The Quantum World Unveiled"></div>
    <div class="seal"><div class="seal-inner">
      <span class="script">Perfect</span><span class="big">GIFT</span><span class="small">FOR THE</span><span class="big">SCIENCE<br>LOVER</span>
    </div></div>
    <div class="ribbon"><div class="a">IDEAL FOR</div><div class="b">SCIENCE STUDENTS</div><div class="c">QUANTUM COMPUTING ENTHUSIASTS</div></div>
  </section>

  <article class="card" style="left:51px">
    <div class="card-head dark"><span class="thin">HISTORY OF</span><em>QUANTUM<br>MECHANICS</em></div>
    <p class="card-body">Explore the fascinating history of quantum mechanics and the brilliant minds behind its development</p>
  </article>
  <article class="card" style="left:201px">
    <div class="card-head light"><span class="thin">FUNDAMENTAL</span>PRINCIPLES OF<br>WAVE-PARTICLE</div>
    <p class="card-body">Grasp the fundamental principles of wave-particle duality, quantum states, and the uncertainty principle</p>
  </article>
  <article class="card" style="left:349px">
    <div class="card-head dark"><span class="thin">QUANTUM</span><em>ENTANGLEMENT</em></div>
    <p class="card-body">Dive into the strange and counterintuitive world of quantum entanglement and its implications for reality itself</p>
  </article>
  <article class="card" style="left:498px">
    <div class="card-head light"><span class="thin">QUANTUM</span>COMPUTING TO<br>CRYPTOGRAPHY</div>
    <p class="card-body">Learn about the cutting-edge applications of quantum mechanics, from quantum computing to cryptography</p>
  </article>

  <section class="contents">
    <h2>IN THIS BOOK YOU WILL FIND</h2>
    <div class="bottom-books" role="img" aria-label="Quantum Physics paperback standing in front of its back cover"></div>
  </section>

  <svg width="0" height="0" style="position:absolute"><defs>
    <symbol id="atom" viewBox="0 0 20 20"><g fill="none" stroke="#f1e52a" stroke-width="1.2">
      <ellipse cx="10" cy="10" rx="8.5" ry="3.4"/><ellipse cx="10" cy="10" rx="8.5" ry="3.4" transform="rotate(60 10 10)"/><ellipse cx="10" cy="10" rx="8.5" ry="3.4" transform="rotate(-60 10 10)"/></g>
      <circle cx="10" cy="10" r="1.6" fill="#f1e52a"/></symbol></defs></svg>

  <div class="chapter" style="top:775px;height:23px"><svg width="15" height="15"><use href="#atom"/></svg>The Quantum World Unveiled</div>
  <div class="chapter" style="top:808px;height:30px"><svg width="15" height="15"><use href="#atom"/></svg>The Mathematical Symphony of Quantum Mechanics</div>
  <div class="chapter" style="top:846px;height:23px"><svg width="15" height="15"><use href="#atom"/></svg>Beyond Classical Boundaries</div>
  <div class="chapter" style="top:880px;height:23px"><svg width="15" height="15"><use href="#atom"/></svg>Quantum Mechanics at Work</div>
  <div class="chapter" style="top:913px;height:30px"><svg width="15" height="15"><use href="#atom"/></svg>Bridging Quantum Mechanics &amp;Relativity</div>
  <div class="chapter" style="top:952px;height:30px"><svg width="15" height="15"><use href="#atom"/></svg>Quantum Paradoxes and Thought Experiments</div>
  <div class="chapter" style="top:990px;height:30px"><svg width="15" height="15"><use href="#atom"/></svg>Quantum Mechanics for the Curious Mind</div>
  <div class="chapter" style="top:1029px;height:30px"><svg width="15" height="15"><use href="#atom"/></svg>Quantum Mechanics Demystified - A Practical Guide</div>
</main>
</body>
</html>
```